Outpost Lattice Advisors – Franchise Growth & Development Presentation

Outpost Lattice Advisors is an outsourced franchise sales organization (FSO) that helps franchisors grow their franchise systems without the expense and risk of hiring an internal franchise development team.

We are seeking a professional PowerPoint presentation that will be used to present our services to franchisors, franchise executives, founders, and growth-stage franchise brands.

The presentation should communicate the value of partnering with Outpost Lattice Advisors, including:

• Fractional franchise sales team versus hiring internal staff
• 30+ years of franchise industry experience
• 550+ franchise sales successes
• Immediate access to established franchise broker relationships
• Proven franchise development processes
• Franchise growth strategy and enterprise value creation
• Potential private equity and exit opportunities through franchise expansion

The presentation should feel like a modern consulting, investment, or growth strategy presentation rather than a typical sales brochure. We want strong visual storytelling, custom infographics, professional diagrams, and clean business-oriented design.

The audience includes business owners, franchise founders, franchise executives, and investors who are evaluating growth strategies for their franchise systems.

Target Market(s)

Primary Audience: Emerging franchisors Growth-stage franchise brands Franchise founders Franchise CEOs Franchise presidents Franchise development executives Secondary Audience: Private equity firms Franchise investors Strategic buyers Franchise consultants

Industry/Entity Type

Franchise Development, Private Equity / Business Expansion

Font styles to use
Other font styles liked:
• Use Montserrat for titles and Open Sans for body text.

Requirements
Must have
• Modern professional business design Consistent branding throughout Custom infographics Comparison graphics Broker network ecosystem graphic Enterprise value graphic Easy-to-read charts and visuals Editable PowerPoint format Professional iconography. www.outpostlatticeadvisors.example as reference for colors
Nice to have
• Franchise-related imagery Subtle growth-themed visuals Timeline graphics Data visualization Private equity / valuation style graphics
Should not have
• Cartoon graphics Clip art Overly busy slides Stock-template appearance Bright neon colors Handwritten fonts Excessive text on slides Juvenile or playful design elements

```html
<!DOCTYPE html>
<html lang="en">
<head>
<meta charset="utf-8">
<title>Outpost Lattice Advisors – Franchise Growth Presentation</title>
<link href="https://fonts.googleapis.com/css2?family=Montserrat:wght@500;600;700;800&family=Open+Sans:ital,wght@0,400;0,600;0,700;1,400&display=swap" rel="stylesheet">
<style>
:root{
  --canvas:#e6e9ee;
  --navy:#0f2a4d;
  --navy-deep:#0a1d38;
  --navy-card:#173861;
  --orange:#f39200;
  --gold:#6e5322;
  --ink:#13294b;
  --grey:#7d8898;
  --line:#dfe3ea;
  --soft:#f4f6f9;
  --white:#ffffff;
}
*{box-sizing:border-box;margin:0;padding:0}
html,body{width:1019px;height:1200px;overflow:hidden;background:var(--canvas)}
body{font-family:"Open Sans",sans-serif;color:var(--ink)}
.canvas{position:relative;width:1019px;height:1200px;overflow:hidden;background:var(--canvas)}
.slide{position:absolute;width:299px;height:169px;border-radius:6px;background:var(--white);overflow:hidden}
.slide.dark{background:radial-gradient(ellipse at 78% 20%,#1d3e69 0%,rgba(29,62,105,0) 55%),linear-gradient(135deg,#0c2140 0%,#0a1a33 100%);color:var(--white)}
.abs{position:absolute}
.eyebrow{position:absolute;left:13.9px;top:12px;font:700 3.5px/1 "Montserrat",sans-serif;letter-spacing:.14em;color:var(--orange);text-transform:uppercase}
.title{position:absolute;left:13.9px;top:17.5px;font:700 8.8px/1.15 "Montserrat",sans-serif;color:var(--ink)}
.dark .title{color:var(--white)}
.lede{position:absolute;left:13.9px;top:37px;font-size:3.4px;color:var(--grey)}
.foot{position:absolute;left:13.9px;bottom:6px;font:600 2.3px/1 "Montserrat",sans-serif;letter-spacing:.16em;color:#a4adba}
.pg{position:absolute;right:14px;bottom:6px;font-size:2.3px;color:#a4adba}
.dark .foot,.dark .pg{color:rgba(255,255,255,.38)}
.ico{display:grid;place-items:center;border-radius:50%;background:var(--navy);color:var(--white)}
.ico svg{width:55%;height:55%}
.ico.or{background:var(--orange)}
.brand{position:absolute;font:800 7.4px/1 "Montserrat",sans-serif;color:var(--white);letter-spacing:.02em}

/* cover */
.cover-title{position:absolute;left:18px;top:56px;font:700 12.3px/1.17 "Montserrat",sans-serif}
.cover-sub{position:absolute;left:18px;top:90px;width:170px;font-size:5.1px;line-height:1.5;color:#c6d0de}
.stat{position:absolute;top:124px}
.stat b{display:block;font:700 10px/1 "Montserrat",sans-serif;color:var(--orange)}
.stat span{display:block;margin-top:3px;font-size:2.9px;line-height:1.35;color:#b7c2d2}

/* toc */
.toc{position:absolute;left:13.9px;top:47px;width:265px;border:.5px solid var(--line)}
.toc-row{display:grid;grid-template-columns:21px 77px 1fr;height:18.4px;border-bottom:.5px solid var(--line)}
.toc-row:last-child{border-bottom:0}
.toc-num{background:var(--navy);color:var(--white);font:700 3.8px/18.4px "Montserrat",sans-serif;text-align:center}
.toc-name{font:700 4.4px/18.4px "Montserrat",sans-serif;padding-left:6px;border-right:.5px solid var(--line)}
.toc-desc{font-size:3.2px;line-height:18.4px;padding-left:8px;color:var(--grey)}

/* barrier cards */
.bcard{position:absolute;width:84px;height:46px;background:var(--soft);border:.5px solid #e3e7ee;border-radius:2px;padding:6px 6px}
.bcard .ico{width:10px;height:10px}
.bcard h4{margin-top:5px;font:700 3.8px/1.2 "Montserrat",sans-serif}
.bcard p{margin-top:3px;font-size:2.6px;line-height:1.45;color:var(--grey)}

/* framework buttons */
.fbtn{position:absolute;width:127px;height:29px;background:var(--navy-card);border-radius:2px;display:flex;align-items:center;gap:5px;padding-left:8px;font:700 4.4px/1 "Montserrat",sans-serif}
.fbtn .ico{width:10px;height:10px}

/* cost matrix */
.mcol{position:absolute;top:40.4px;width:124.5px}
.mhead{height:12.8px;font:700 3.6px/12.8px "Montserrat",sans-serif;text-align:center;color:var(--white)}
.mrow{height:13.35px;display:flex;align-items:center;justify-content:space-between;padding:0 4px;font-size:3.1px;border-bottom:.5px solid var(--line)}
.mrow:nth-child(odd){background:#f6f7f9}
.mcol.int .mhead{background:var(--navy)}
.mcol.int .mrow{color:#9aa3b1}
.mcol.ola .mhead{background:var(--orange)}
.mcol.ola .mrow{font-weight:700;color:var(--ink)}
.tag{width:5px;height:5px;border-radius:50%;display:grid;place-items:center;color:var(--white)}
.tag svg{width:80%;height:80%}
.tag.no{background:#5b6676}
.tag.yes{background:var(--orange)}

/* services */
.scard{position:absolute;width:64px;height:48.5px;background:rgba(31,66,112,.55);border-radius:2px;text-align:center;padding-top:10px}
.scard .ico{width:12px;height:12px;margin:0 auto}
.scard p{margin-top:7px;font:700 3.6px/1.3 "Montserrat",sans-serif;padding:0 3px}

/* experience */
.big{position:absolute;left:13.9px;font:800 29px/1 "Montserrat",sans-serif;color:var(--white)}
.big-lbl{position:absolute;left:13.9px;font-size:4.8px;color:var(--orange)}
.exp{position:absolute;left:148.7px;display:flex;align-items:center;gap:8px;font:700 4.7px/1.3 "Montserrat",sans-serif}
.exp .ico{width:23px;height:23px}

/* success */
.case{position:absolute;top:47px;width:86.7px;height:90px;background:var(--white);border:.5px solid var(--line);box-shadow:0 .5px 2px rgba(15,42,77,.08);text-align:center}
.case-band{height:21px;background:var(--navy);position:relative}
.case-band .ico{position:absolute;left:50%;top:6px;transform:translateX(-50%);width:11px;height:11px}
.case .num{margin-top:4.5px;font:700 2.9px/1 "Montserrat",sans-serif;color:var(--orange);letter-spacing:.05em}
.case h4{margin-top:5px;font:700 4.6px/1.2 "Montserrat",sans-serif}
.case p{margin:6px 10px 0;font-size:2.6px;line-height:1.5;color:var(--grey)}
.case p b{color:var(--ink)}

/* enterprise tables */
.tlabel{position:absolute;top:56.5px;font:700 3.1px/1 "Montserrat",sans-serif;letter-spacing:.1em}
.vtable{position:absolute;top:64px;border-collapse:collapse;font-size:3.1px}
.vtable th{background:var(--navy);color:var(--white);font:700 3.1px/1 "Montserrat",sans-serif;height:10.4px;text-align:center;border-right:.5px solid #2a4670}
.vtable th:first-child{text-align:left;padding-left:2.5px}
.vtable td{height:11.5px;text-align:center;border-bottom:.5px solid var(--line);color:#4b5768}
.vtable td:first-child{text-align:left;padding-left:2.5px;font-weight:700;color:var(--ink)}
.takeaway{position:absolute;left:13.9px;top:115.5px;width:260px;height:30px;background:var(--soft);border:.5px solid var(--line);border-radius:2px;padding:5.5px 9px}
.takeaway h5{font:700 3.9px/1 "Montserrat",sans-serif}
.takeaway p{margin-top:3px;font-size:3.1px;line-height:1.5;color:var(--grey)}

/* exit */
.xcard{position:absolute;top:49.7px;width:50.3px;height:64.7px;background:rgba(31,66,112,.5);border-radius:2px;text-align:center;padding-top:9px}
.xcard .ico{width:12px;height:12px;margin:0 auto}
.xcard p{margin-top:13px;font:700 3.8px/1.3 "Montserrat",sans-serif;padding:0 3px}
.goldbar{position:absolute;left:13.9px;top:120px;width:270.4px;height:22.6px;background:var(--gold);border-radius:1.5px;font:700 4.3px/22.6px "Montserrat",sans-serif;text-align:center}

/* different */
.dcard{position:absolute;width:64px;height:43.3px;background:var(--soft);border:.5px solid #e3e7ee;border-radius:2px;text-align:center;padding-top:7px}
.dcard .ico{width:11px;height:11px;margin:0 auto}
.dcard p{margin-top:8px;font:700 3.7px/1.3 "Montserrat",sans-serif;padding:0 3px}
.dcard.hi{background:var(--navy);color:var(--white);border-color:var(--navy)}
.dcard.hi .ico{background:var(--navy-card)}

/* engagement */
.ecard{position:absolute;top:48.5px;width:52px;height:89.5px;background:var(--soft);border:.5px solid #e3e7ee;border-radius:2px;text-align:center;padding-top:7px}
.ecard .ico{width:12px;height:12px;margin:0 auto}
.ecard h4{margin-top:6px;font:700 3.7px/1.3 "Montserrat",sans-serif;padding:0 3px}
.ecard p{position:absolute;left:3px;right:3px;bottom:7px;font-size:2.6px;line-height:1.45;color:var(--grey)}
.ecard.hi{background:var(--navy);border-color:var(--navy);color:var(--white)}
.ecard.hi .ico{background:var(--navy-card)}
.ecard.hi p{color:#b6c1d2}

/* summary */
.sumbox{position:absolute;top:50.3px;width:123.6px;height:67px;border:.7px solid var(--navy);border-radius:2px;padding:6px 8px}
.sumitem{display:flex;align-items:center;gap:5px;height:18.5px;font-size:3.3px;line-height:1.4}
.sumitem .tag{width:6px;height:6px;flex:none}
.quote{position:absolute;left:13.9px;top:130px;width:260px;height:18.5px;background:var(--soft);border:.5px solid var(--line);border-radius:2px;font-style:italic;font-size:3.2px;line-height:18.5px;padding-left:8px;color:var(--grey)}

/* cta */
.cta-title{position:absolute;left:18.5px;top:57px;font:700 12.6px/1 "Montserrat",sans-serif}
.cta-sub{position:absolute;left:18.5px;top:77px;font-size:5.3px;color:var(--orange)}
.cta-btn{position:absolute;left:18.5px;top:99.2px;width:71.6px;height:13.8px;border-radius:7px;background:var(--orange);color:var(--navy-deep);font:700 4.2px/13.8px "Montserrat",sans-serif;text-align:center}
.contact{position:absolute;left:18.5px;display:flex;align-items:center;gap:4px;font-size:3.7px;color:#d3dbe6}
.contact .ico{width:7px;height:7px}
svg text{font-family:"Montserrat",sans-serif}
</style>
</head>
<body>
<svg width="0" height="0" style="position:absolute" aria-hidden="true">
  <defs>
    <symbol id="users" viewBox="0 0 24 24"><circle cx="9" cy="8" r="3.3" fill="currentColor"/><circle cx="16.6" cy="9" r="2.6" fill="currentColor"/><path fill="currentColor" d="M2.8 19.5c0-3.6 2.7-6.2 6.2-6.2s6.2 2.6 6.2 6.2z"/><path fill="currentColor" d="M15.2 19.5c0-2-.5-3.7-1.6-5 .9-.6 2-.9 3.1-.9 2.8 0 4.8 2.2 4.8 5.9z"/></symbol>
    <symbol id="user" viewBox="0 0 24 24"><circle cx="12" cy="7.5" r="4.2" fill="currentColor"/><path fill="currentColor" d="M4 21.5c0-4.6 3.6-7.6 8-7.6s8 3 8 7.6z"/></symbol>
    <symbol id="funnel" viewBox="0 0 24 24"><path fill="currentColor" d="M3 4h18l-7 8.5V19l-4 2.2v-8.7z"/></symbol>
    <symbol id="search" viewBox="0 0 24 24"><circle cx="10" cy="10" r="5.8" fill="none" stroke="currentColor" stroke-width="2.6"/><path d="M14.5 14.5l5.5 5.5" stroke="currentColor" stroke-width="2.8" stroke-linecap="round"/></symbol>
    <symbol id="phone" viewBox="0 0 24 24"><path fill="currentColor" d="M6.6 10.8a15 15 0 006.6 6.6l2.2-2.2c.3-.3.7-.4 1-.2 1.1.4 2.3.6 3.6.6.6 0 1 .4 1 1V20c0 .6-.4 1-1 1C10.6 21 3 13.4 3 4c0-.6.4-1 1-1h3.5c.6 0 1 .4 1 1 0 1.3.2 2.5.6 3.6.1.3 0 .7-.2 1z"/></symbol>
    <symbol id="network" viewBox="0 0 24 24"><rect x="9" y="2" width="6" height="5" rx="1" fill="currentColor"/><rect x="2" y="16" width="6" height="5" rx="1" fill="currentColor"/><rect x="9" y="16" width="6" height="5" rx="1" fill="currentColor"/><rect x="16" y="16" width="6" height="5" rx="1" fill="currentColor"/><path fill="currentColor" d="M11.2 7h1.6v4H19v5h-1.6v-3.4h-4.6V16h-1.6v-3.4H6.6V16H5v-5h6.2z"/></symbol>
    <symbol id="db" viewBox="0 0 24 24"><ellipse cx="12" cy="5" rx="8" ry="3" fill="currentColor"/><path fill="currentColor" d="M4 7.5c0 1.7 3.6 3 8 3s8-1.3 8-3V11c0 1.7-3.6 3-8 3s-8-1.3-8-3zM4 13.5c0 1.7 3.6 3 8 3s8-1.3 8-3V19c0 1.7-3.6 3-8 3s-8-1.3-8-3z"/></symbol>
    <symbol id="globe" viewBox="0 0 24 24"><g fill="none" stroke="currentColor" stroke-width="2"><circle cx="12" cy="12" r="9"/><path d="M3 12h18M12 3c3.2 3 3.2 15 0 18M12 3c-3.2 3-3.2 15 0 18"/></g></symbol>
    <symbol id="flow" viewBox="0 0 24 24"><rect x="2" y="3" width="7" height="6" rx="1" fill="currentColor"/><rect x="15" y="3" width="7" height="6" rx="1" fill="currentColor"/><rect x="9" y="15" width="7" height="6" rx="1" fill="currentColor"/><path fill="currentColor" d="M9 5.2h6v1.6H9zM11.7 9h1.6v6h-1.6z"/></symbol>
    <symbol id="award" viewBox="0 0 24 24"><path fill="currentColor" d="M8.3 13.5L6.5 22l5.5-3 5.5 3-1.8-8.5z"/><circle cx="12" cy="9" r="6.5" fill="currentColor"/></symbol>
    <symbol id="hand" viewBox="0 0 24 24"><path fill="currentColor" d="M1.5 8.5l4.5-2 5 2 3-1.3 4 1.3 4.5 2v5.5l-3 1-5 4-2.8-1.8-4.2-1.2-6-4.5z"/></symbol>
    <symbol id="star" viewBox="0 0 24 24"><path fill="currentColor" d="M12 2l3 6.5 7 .8-5.2 4.8 1.5 7L12 17.5 5.7 21l1.5-7L2 9.3l7-.8z"/></symbol>
    <symbol id="rocket" viewBox="0 0 24 24"><path fill="currentColor" d="M14 3c3.5 0 6 .5 7 1.5-.1 4-2.2 7.3-5.5 9.5l.5 4-3.5 3-1-4-3.5-3.5-4-1 3-3.5 4 .5C11 6.6 12 4 14 3zM6 16c-1 1-2.5 4-2.5 5 1 0 4-1.5 5-2.5z"/></symbol>
    <symbol id="gear" viewBox="0 0 24 24"><circle cx="12" cy="12" r="8.6" fill="none" stroke="currentColor" stroke-width="3" stroke-dasharray="2.6 2.2"/><circle cx="12" cy="12" r="6.8" fill="currentColor"/></symbol>
    <symbol id="chart" viewBox="0 0 24 24"><path fill="currentColor" d="M3 20h18v2H3zM4 16l5-5 4 3 7-7 1.4 1.4L13 17l-4-3-3.6 3.6z"/></symbol>
    <symbol id="doc" viewBox="0 0 24 24"><path fill="currentColor" d="M5 2h9.5L20 7.5V22H5z"/></symbol>
    <symbol id="cal" viewBox="0 0 24 24"><path fill="currentColor" d="M3.5 5h17v16h-17zM7 2h2v4H7zM15 2h2v4h-2z"/></symbol>
    <symbol id="check" viewBox="0 0 24 24"><path d="M5 12.5l4.5 4.5L19 7.5" fill="none" stroke="currentColor" stroke-width="3.4" stroke-linecap="round" stroke-linejoin="round"/></symbol>
    <symbol id="xmark" viewBox="0 0 24 24"><path d="M7 7l10 10M17 7L7 17" fill="none" stroke="currentColor" stroke-width="3.4" stroke-linecap="round"/></symbol>
    <symbol id="share" viewBox="0 0 24 24"><circle cx="18" cy="5" r="3.2" fill="currentColor"/><circle cx="6" cy="12" r="3.2" fill="currentColor"/><circle cx="18" cy="19" r="3.2" fill="currentColor"/><path d="M18 5L6 12l12 7" fill="none" stroke="currentColor" stroke-width="2"/></symbol>
    <symbol id="monitor" viewBox="0 0 24 24"><path fill="currentColor" d="M2 4h20v13H2zM9 18.5h6v2.5H9z"/></symbol>
    <symbol id="chat" viewBox="0 0 24 24"><path fill="currentColor" d="M3 4h18v12H9l-6 4.5z"/></symbol>
    <symbol id="bank" viewBox="0 0 24 24"><path fill="currentColor" d="M12 2l10 5v2H2V7zM4 10h3v8H4zM10.5 10h3v8h-3zM17 10h3v8h-3zM2 19h20v3H2z"/></symbol>
    <symbol id="refresh" viewBox="0 0 24 24"><g fill="none" stroke="currentColor" stroke-width="2.6"><path d="M19.5 12a7.5 7.5 0 01-13.6 4.3M4.5 12a7.5 7.5 0 0113.6-4.3"/></g><path fill="currentColor" d="M20 4v6h-6zM4 20v-6h6z"/></symbol>
    <symbol id="mail" viewBox="0 0 24 24"><path fill="currentColor" d="M2 5h20v14H2z"/></symbol>
    <symbol id="pin" viewBox="0 0 24 24"><path fill="currentColor" d="M12 2a7 7 0 017 7c0 5-7 13-7 13S5 14 5 9a7 7 0 017-7z"/></symbol>
  </defs>
</svg>

<main class="canvas">

<!-- 01 Cover -->
<section class="slide dark" style="left:46px;top:46px">
  <div class="brand" style="left:18px;top:24px">OUTPOST LATTICE ADVISORS</div>
  <h1 class="cover-title">Outsourced Franchise Sales<br>&amp; Growth Experts</h1>
  <p class="cover-sub">Helping franchisors grow faster without the cost and risk of building an internal franchise development team.</p>
  <div class="stat" style="left:18px"><b>30+</b><span>Years of Franchise<br>Industry Experience</span></div>
  <div class="stat" style="left:89px"><b>500+</b><span>Franchise Sales<br>Successes</span></div>
  <div class="stat" style="left:159.5px"><b>100%</b><span>Fractional, Outsourced<br>Development Model</span></div>
  <div class="pg">01</div>
</section>

<!-- 02 Contents -->
<section class="slide" style="left:359px;top:46px">
  <div class="eyebrow">Agenda Briefing</div>
  <h2 class="title">Table of Content</h2>
  <div class="toc">
    <div class="toc-row"><div class="toc-num">01</div><div class="toc-name">The Challenge</div><div class="toc-desc">Why franchise growth stalls without dedicated development support.</div></div>
    <div class="toc-row"><div class="toc-num">02</div><div class="toc-name">The OLA Advantage</div><div class="toc-desc">A fractional team and broker network built for immediate impact.</div></div>
    <div class="toc-row"><div class="toc-num">03</div><div class="toc-name">Our Process</div><div class="toc-desc">How qualified leads move from first contact to franchise award.</div></div>
    <div class="toc-row"><div class="toc-num">04</div><div class="toc-name">Financial Mechanics</div><div class="toc-desc">How franchise growth builds recurring revenue and enterprise value.</div></div>
    <div class="toc-row"><div class="toc-num">05</div><div class="toc-name">Engagement &amp; Next Steps</div><div class="toc-desc">Flexible ways to begin working together.</div></div>
  </div>
  <div class="foot">OUTPOST LATTICE ADVISORS</div><div class="pg">02</div>
</section>

<!-- 03 Challenge -->
<section class="slide" style="left:672px;top:46px">
  <div class="eyebrow">The Challenge</div>
  <h2 class="title">Operational Barriers to Scale</h2>
  <div class="bcard" style="left:13.9px;top:41.6px"><div class="ico"><svg><use href="#users"/></svg></div><h4>Limited Franchise Sales Resources</h4><p>No dedicated team focused on candidate outreach and follow-up.</p></div>
  <div class="bcard" style="left:103.4px;top:41.6px"><div class="ico"><svg><use href="#user"/></svg></div><h4>Founder Wearing Too Many Hats</h4><p>Growth competes with day-to-day operations for attention.</p></div>
  <div class="bcard" style="left:193px;top:41.6px"><div class="ico"><svg><use href="#phone"/></svg></div><h4>Inconsistent Lead Follow-Up</h4><p>Promising candidates go cold without a structured process.</p></div>
  <div class="bcard" style="left:13.9px;top:93.6px"><div class="ico"><svg><use href="#search"/></svg></div><h4>Difficulty Recruiting Franchisees</h4><p>Sourcing qualified, well-capitalized candidates takes expertise.</p></div>
  <div class="bcard" style="left:103.4px;top:93.6px"><div class="ico"><svg><use href="#network"/></svg></div><h4>Lack of Broker Relationships</h4><p>No access to the referral networks that drive consistent flow.</p></div>
  <div class="bcard" style="left:193px;top:93.6px"><div class="ico"><svg><use href="#db"/></svg></div><h4>High Cost of Internal Development Staff</h4><p>Salaries and overhead add up long before results do.</p></div>
  <div class="foot">OUTPOST LATTICE ADVISORS</div><div class="pg">03</div>
</section>

<!-- 04 Framework -->
<section class="slide dark" style="left:46px;top:234px">
  <div class="eyebrow">The Strategic Framework</div>
  <h2 class="title">Why Outpost Lattice Advisors</h2>
  <div class="fbtn" style="left:13.9px;top:48.5px"><div class="ico or"><svg><use href="#hand"/></svg></div>Fractional Franchise Sales Team</div>
  <div class="fbtn" style="left:147.3px;top:48.5px"><div class="ico or"><svg><use href="#award"/></svg></div>30+ Years Franchise Industry Experience</div>
  <div class="fbtn" style="left:13.9px;top:83.2px"><div class="ico or"><svg><use href="#chart"/></svg></div>500+ Franchise Sales Successes</div>
  <div class="fbtn" style="left:147.3px;top:83.2px"><div class="ico or"><svg><use href="#rocket"/></svg></div>Immediate Execution</div>
  <div class="fbtn" style="left:13.9px;top:117.9px"><div class="ico or"><svg><use href="#gear"/></svg></div>Proven Systems and Processes</div>
  <div class="fbtn" style="left:147.3px;top:117.9px"><div class="ico or"><svg><use href="#network"/></svg></div>Deep Broker Network Relationships</div>
  <div class="foot">OUTPOST LATTICE ADVISORS</div><div class="pg">04</div>
</section>

<!-- 05 Cost matrix -->
<section class="slide" style="left:359px;top:234px">
  <div class="eyebrow">The Cost of Hiring vs. Outsourcing</div>
  <h2 class="title">Cost-Efficiency Matrix</h2>
  <div class="mcol int" style="left:13.9px">
    <div class="mhead">Internal Development Director</div>
    <div class="mrow">Recruiting costs<span class="tag no"><svg><use href="#xmark"/></svg></span></div>
    <div class="mrow">Salary<span class="tag no"><svg><use href="#xmark"/></svg></span></div>
    <div class="mrow">Benefits<span class="tag no"><svg><use href="#xmark"/></svg></span></div>
    <div class="mrow">Payroll taxes<span class="tag no"><svg><use href="#xmark"/></svg></span></div>
    <div class="mrow">Training<span class="tag no"><svg><use href="#xmark"/></svg></span></div>
    <div class="mrow">Ramp up period<span class="tag no"><svg><use href="#xmark"/></svg></span></div>
    <div class="mrow">Unknown performance<span class="tag no"><svg><use href="#xmark"/></svg></span></div>
  </div>
  <div class="mcol ola" style="left:149.6px">
    <div class="mhead">Outpost Lattice Advisors</div>
    <div class="mrow">Fractional investment<span class="tag yes"><svg><use href="#check"/></svg></span></div>
    <div class="mrow">Entire team of experts<span class="tag yes"><svg><use href="#check"/></svg></span></div>
    <div class="mrow">Immediate launch<span class="tag yes"><svg><use href="#check"/></svg></span></div>
    <div class="mrow">Proven processes<span class="tag yes"><svg><use href="#check"/></svg></span></div>
    <div class="mrow">Existing relationships<span class="tag yes"><svg><use href="#check"/></svg></span></div>
    <div class="mrow">Scalable growth<span class="tag yes"><svg><use href="#check"/></svg></span></div>
    <div class="mrow">Established track record<span class="tag yes"><svg><use href="#check"/></svg></span></div>
  </div>
  <div class="foot">OUTPOST LATTICE ADVISORS</div><div class="pg">05</div>
</section>

<!-- 06 Day one -->
<section class="slide" style="left:672px;top:234px">
  <div class="eyebrow">Speed to Market</div>
  <h2 class="title">What Takes Years to Build,<br>You Get on Day One</h2>
  <svg class="abs" style="left:0;top:0" width="299" height="169" viewBox="0 0 299 169">
    <circle cx="171.6" cy="93.6" r="46" fill="none" stroke="#f39200" stroke-width="1.8"/>
    <circle cx="171.6" cy="93.6" r="18" fill="#0f2a4d"/>
    <text x="171.6" y="95.8" text-anchor="middle" font-size="6.4" font-weight="700" fill="#fff">DAY 1</text>
    <g fill="#fff" stroke="#d9dee6" stroke-width=".5">
      <circle cx="171.6" cy="46.2" r="11"/><circle cx="208.5" cy="63.5" r="11"/><circle cx="217.2" cy="105.1" r="11"/><circle cx="192.4" cy="135.8" r="11"/><circle cx="151.9" cy="134.6" r="11"/><circle cx="126.5" cy="104" r="11"/><circle cx="135.2" cy="63.5" r="11"/>
    </g>
    <g color="#0f2a4d">
      <use href="#network" x="166.1" y="40.7" width="11" height="11"/>
      <use href="#user" x="203" y="58" width="11" height="11"/>
      <use href="#funnel" x="211.7" y="99.6" width="11" height="11"/>
      <use href="#flow" x="186.9" y="130.3" width="11" height="11"/>
      <use href="#users" x="146.4" y="129.1" width="11" height="11"/>
      <use href="#globe" x="121" y="98.5" width="11" height="11"/>
      <use href="#db" x="129.7" y="58" width="11" height="11"/>
    </g>
    <g font-size="3.3" font-weight="700" fill="#13294b">
      <text x="171.6" y="23" text-anchor="middle">Franchise Broker</text><text x="171.6" y="27" text-anchor="middle">Relationships</text>
      <text x="241" y="63" text-anchor="middle">Franchise Sales</text><text x="241" y="67" text-anchor="middle">Expertise</text>
      <text x="255" y="102" text-anchor="middle">Lead Qualification</text><text x="255" y="106" text-anchor="middle">Systems</text>
      <text x="233" y="144" text-anchor="middle">Franchise Development</text><text x="233" y="148" text-anchor="middle">Processes</text>
      <text x="114" y="145" text-anchor="middle">Candidate Nurturing</text><text x="114" y="149" text-anchor="middle">Systems</text>
      <text x="93" y="102" text-anchor="middle">Industry</text><text x="93" y="106" text-anchor="middle">Connections</text>
      <text x="99" y="64" text-anchor="middle">CRM &amp; Reporting</text><text x="99" y="68" text-anchor="middle">Infrastructure</text>
    </g>
  </svg>
  <div class="foot">OUTPOST LATTICE ADVISORS</div><div class="pg">06</div>
</section>

<!-- 07 Broker network -->
<section class="slide" style="left:46px;top:422px">
  <div class="eyebrow">Broker Network Ecosystem</div>
  <h2 class="title">Instant Access to the Franchise Broker Community</h2>
  <p class="lede" style="font-style:italic;top:35.5px">We spent over 20 years building these relationships so your brand doesn't have to.</p>
  <svg class="abs" style="left:0;top:0" width="170" height="169" viewBox="0 0 170 169">
    <g stroke="#0f2a4d" stroke-width=".8"><line x1="83.8" y1="100.5" x2="83.8" y2="67"/><line x1="83.8" y1="100.5" x2="120" y2="91.6"/><line x1="83.8" y1="100.5" x2="105.5" y2="129.7"/><line x1="83.8" y1="100.5" x2="61" y2="129.7"/><line x1="83.8" y1="100.5" x2="47.4" y2="91.6"/></g>
    <circle cx="83.8" cy="100.5" r="17.5" fill="#0f2a4d"/>
    <text x="83.8" y="103" text-anchor="middle" font-size="7" font-weight="700" fill="#fff">OLA</text>
    <g fill="#fff" stroke="#dde2ea" stroke-width=".5"><circle cx="83.8" cy="67" r="7.5"/><circle cx="120" cy="91.6" r="7.5"/><circle cx="105.5" cy="129.7" r="7.5"/><circle cx="61" cy="129.7" r="7.5"/><circle cx="47.4" cy="91.6" r="7.5"/></g>
    <g color="#0f2a4d"><use href="#user" x="79.8" y="63" width="8" height="8"/><use href="#network" x="116" y="87.6" width="8" height="8"/><use href="#hand" x="101.5" y="125.7" width="8" height="8"/><use href="#share" x="57" y="125.7" width="8" height="8"/><use href="#star" x="43.4" y="87.6" width="8" height="8"/></g>
    <g font-size="2.9" font-weight="700" fill="#13294b">
      <text x="83.8" y="55" text-anchor="middle">Franchise Consultants</text>
      <text x="129" y="90.5">Broker</text><text x="129" y="94">Networks</text>
      <text x="33" y="90.5" text-anchor="middle">Franchise</text><text x="33" y="94" text-anchor="middle">Influencers</text>
      <text x="61" y="142" text-anchor="middle">Referral</text><text x="61" y="145.5" text-anchor="middle">Sources</text>
      <text x="105.5" y="142" text-anchor="middle">Industry</text><text x="105.5" y="145.5" text-anchor="middle">Partners</text>
    </g>
  </svg>
  <div class="abs" style="left:170px;top:64px;font:700 3.6px/1 Montserrat,sans-serif">Trusted across the leading franchise broker networks</div>
  <div class="abs" role="img" aria-label="Partner network badge" style="left:170px;top:76px;width:36px;height:11px;background:var(--navy);border-radius:1px"></div>
  <div class="abs" role="img" aria-label="Partner network badge" style="left:209px;top:76px;width:36px;height:11px;background:var(--navy);border-radius:1px"></div>
  <div class="abs" role="img" aria-label="Partner network badge" style="left:248px;top:76px;width:36px;height:11px;background:var(--navy);border-radius:1px"></div>
  <div class="abs" role="img" aria-label="Partner network badge" style="left:170px;top:91.6px;width:36px;height:11px;background:var(--navy);border-radius:1px"></div>
  <div class="abs" role="img" aria-label="Partner network badge" style="left:209px;top:91.6px;width:36px;height:11px;background:var(--navy);border-radius:1px"></div>
  <div class="abs" role="img" aria-label="Partner network badge" style="left:248px;top:91.6px;width:36px;height:11px;background:var(--navy);border-radius:1px"></div>
  <div class="abs" style="left:170px;top:106px;width:114px;height:34px;background:var(--soft);border:.5px solid var(--line);border-radius:2px;padding:5px 6px">
    <div style="font:700 3.6px/1 Montserrat,sans-serif">Why this matters</div>
    <p style="margin-top:4px;font-size:2.6px;line-height:1.55;color:var(--grey)">Building broker trust typically takes years of consistent execution. Partnering with us puts your brand in front of qualified candidates through channels already earning their trust today.</p>
  </div>
  <div class="foot">OUTPOST LATTICE ADVISORS</div><div class="pg">07</div>
</section>

<!-- 08 Process -->
<section class="slide" style="left:359px;top:422px">
  <div class="eyebrow">Development Process</div>
  <h2 class="title">Our Franchise Development Process</h2>
  <svg class="abs" style="left:0;top:0" width="299" height="169" viewBox="0 0 299 169">
    <line x1="29.5" y1="71" x2="270.4" y2="71" stroke="#f39200" stroke-width=".8" stroke-dasharray="1 2"/>
    <g fill="#0f2a4d"><circle cx="29.5" cy="71" r="12"/><circle cx="69.9" cy="71" r="12"/><circle cx="109.8" cy="71" r="12"/><circle cx="149.6" cy="71" r="12"/><circle cx="190" cy="71" r="12"/><circle cx="230" cy="71" r="12"/></g>
    <circle cx="270.4" cy="71" r="12" fill="#f39200"/>
    <g fill="#4a5c78"><rect x="17" y="56" width="5.5" height="5.5"/><rect x="57.4" y="56" width="5.5" height="5.5"/><rect x="97.3" y="56" width="5.5" height="5.5"/><rect x="137.1" y="56" width="5.5" height="5.5"/><rect x="177.5" y="56" width="5.5" height="5.5"/><rect x="217.5" y="56" width="5.5" height="5.5"/><rect x="257.9" y="56" width="5.5" height="5.5"/></g>
    <g font-size="3" font-weight="700" fill="#fff" text-anchor="middle"><text x="19.75" y="60">1</text><text x="60.15" y="60">2</text><text x="100.05" y="60">3</text><text x="139.85" y="60">4</text><text x="180.25" y="60">5</text><text x="220.25" y="60">6</text><text x="260.65" y="60">7</text></g>
    <g color="#fff"><use href="#search" x="24" y="65.5" width="11" height="11"/><use href="#funnel" x="64.4" y="65.5" width="11" height="11"/><use href="#monitor" x="104.3" y="65.5" width="11" height="11"/><use href="#doc" x="144.1" y="65.5" width="11" height="11"/><use href="#check" x="184.5" y="65.5" width="11" height="11"/><use href="#cal" x="224.5" y="65.5" width="11" height="11"/></g>
    <use href="#award" x="264.9" y="65.5" width="11" height="11" color="#0f2a4d"/>
    <g font-size="3.4" font-weight="700" fill="#13294b" text-anchor="middle"><text x="29.5" y="95.5">Lead</text><text x="69.9" y="95.5">Qualification</text><text x="109.8" y="95.5">Education</text><text x="149.6" y="95.5">FDD Review</text><text x="190" y="95.5">Validation</text><text x="230" y="95.5">Discovery Day</text><text x="270.4" y="95.5">Franchise Award</text></g>
    <g font-family="Open Sans,sans-serif" font-size="2.4" fill="#a3acb9" text-anchor="middle">
      <text x="29.5" y="101">We attract and capture</text><text x="29.5" y="104">potential franchise</text><text x="29.5" y="107">candidates.</text>
      <text x="69.9" y="101">We qualify each candidate</text><text x="69.9" y="104">to ensure alignment with</text><text x="69.9" y="107">your ideal profile.</text>
      <text x="109.8" y="101">We educate candidates</text><text x="109.8" y="104">on your brand, business</text><text x="109.8" y="107">model and opportunity.</text>
      <text x="149.6" y="101">Candidates review your</text><text x="149.6" y="104">FDD with our guidance</text><text x="149.6" y="107">and support.</text>
      <text x="190" y="101">Candidate validates</text><text x="190" y="104">their fit, capabilities and</text><text x="190" y="107">commitment.</text>
      <text x="230" y="101">Candidates visit, meet your</text><text x="230" y="104">team and experience your</text><text x="230" y="107">brand.</text>
      <text x="270.4" y="101">The right candidate. The</text><text x="270.4" y="104">right time. The right</text><text x="270.4" y="107">partnership.</text>
    </g>
  </svg>
  <div class="abs" style="left:34px;top:127px;width:231px;height:25px;background:var(--soft);border:.5px solid var(--line);border-radius:2px;font-style:italic;font-size:3.1px;line-height:1.55;color:var(--grey);text-align:center;padding:6px 12px">A repeatable, structured path from first contact to a confident franchise award, with no step skipped and no candidate left waiting.</div>
  <div class="foot">OUTPOST LATTICE ADVISORS</div><div class="pg">08</div>
</section>

<!-- 09 Services -->
<section class="slide dark" style="left:672px;top:422px">
  <div class="eyebrow">Services We Provide</div>
  <h2 class="title">Services We Provide</h2>
  <div class="scard" style="left:13.9px;top:41.6px"><div class="ico or"><svg><use href="#doc"/></svg></div><p>FDD / Operations Review</p></div>
  <div class="scard" style="left:82.6px;top:41.6px"><div class="ico or"><svg><use href="#hand"/></svg></div><p>Franchise Sales Outsourcing</p></div>
  <div class="scard" style="left:150.8px;top:41.6px"><div class="ico or"><svg><use href="#funnel"/></svg></div><p>Lead Qualification</p></div>
  <div class="scard" style="left:219.5px;top:41.6px"><div class="ico or"><svg><use href="#users"/></svg></div><p>Candidate Nurturing</p></div>
  <div class="scard" style="left:13.9px;top:96.6px"><div class="ico or"><svg><use href="#cal"/></svg></div><p>Discovery Day Coordination</p></div>
  <div class="scard" style="left:82.6px;top:96.6px"><div class="ico or"><svg><use href="#network"/></svg></div><p>Broker Recruitment &amp; Engagement</p></div>
  <div class="scard" style="left:150.8px;top:96.6px"><div class="ico or"><svg><use href="#db"/></svg></div><p>CRM Management</p></div>
  <div class="scard" style="left:219.5px;top:96.6px"><div class="ico or"><svg><use href="#chart"/></svg></div><p>Reporting and Forecasting</p></div>
  <div class="foot">OUTPOST LATTICE ADVISORS</div><div class="pg">09</div>
</section>

<!-- 10 Referral engine -->
<section class="slide" style="left:46px;top:609px">
  <div class="eyebrow">Referral Engine</div>
  <h2 class="title">Building a Referral Engine for Your Brand</h2>
  <svg class="abs" style="left:0;top:0" width="299" height="169" viewBox="0 0 299 169">
    <circle cx="146" cy="101" r="35" fill="none" stroke="#0f2a4d" stroke-width=".6"/>
    <circle cx="146" cy="101" r="20" fill="#0f2a4d"/>
    <text x="146" y="100" text-anchor="middle" font-size="4.2" font-weight="700" fill="#fff">REFERRAL</text>
    <text x="146" y="105.5" text-anchor="middle" font-size="4.2" font-weight="700" fill="#fff">ENGINE</text>
    <g fill="#fff" stroke="#f39200" stroke-width=".7"><circle cx="146" cy="66" r="9"/><circle cx="181" cy="101" r="9"/><circle cx="146" cy="136" r="9"/><circle cx="111" cy="101" r="9"/></g>
    <g color="#f39200"><use href="#monitor" x="141" y="61" width="10" height="10"/><use href="#monitor" x="176" y="96" width="10" height="10"/><use href="#chat" x="141" y="131" width="10" height="10"/><use href="#share" x="106" y="96" width="10" height="10"/></g>
    <g font-size="4" font-weight="700" fill="#13294b"><text x="146" y="52" text-anchor="middle">Broker &amp; Consultant Education</text><text x="196" y="102.4">Brand Presentations</text><text x="94" y="102.4" text-anchor="end">Referral Generation</text><text x="146" y="153.5" text-anchor="middle">Ongoing Communication</text></g>
  </svg>
  <div class="foot">OUTPOST LATTICE ADVISORS</div><div class="pg">10</div>
</section>

<!-- 11 Experience -->
<section class="slide dark" style="left:359px;top:609px">
  <div class="eyebrow">Proven Authority</div>
  <h2 class="title">Why Experience Matters</h2>
  <div class="big" style="top:50px">500+</div>
  <div class="big-lbl" style="top:79px">Franchise Sales Successes</div>
  <div class="big" style="top:99px">30+</div>
  <div class="big-lbl" style="top:128px">Years Industry Experience</div>
  <div class="exp" style="top:49px"><div class="ico or"><svg><use href="#users"/></svg></div>Thousands of franchise<br>candidates evaluated</div>
  <div class="exp" style="top:80.9px"><div class="ico or"><svg><use href="#network"/></svg></div>Extensive broker network<br>relationships</div>
  <div class="exp" style="top:112.1px"><div class="ico or"><svg><use href="#gear"/></svg></div>Multi-brand franchise<br>development expertise</div>
  <div class="foot">OUTPOST LATTICE ADVISORS</div><div class="pg">11</div>
</section>

<!-- 12 Success stories -->
<section class="slide" style="left:672px;top:609px">
  <div class="eyebrow">Proven Performance</div>
  <h2 class="title">Success Stories</h2>
  <div class="case" style="left:13.9px"><div class="case-band"><div class="ico or"><svg><use href="#star"/></svg></div></div><div class="num">Case Study 01</div><h4>Emerging Brand Growth</h4><p>Franchisor type: Service brand, 0 units at launch</p><p><b>Outcome:</b> Awarded units within first 12 months of partnership</p></div>
  <div class="case" style="left:106.3px"><div class="case-band"><div class="ico or"><svg><use href="#star"/></svg></div></div><div class="num">Case Study 02</div><h4>Multi-Market Expansion</h4><p>Franchisor type: Retail brand, regional footprint</p><p><b>Outcome:</b> Expanded into new territories through broker channels</p></div>
  <div class="case" style="left:198.8px"><div class="case-band"><div class="ico or"><svg><use href="#star"/></svg></div></div><div class="num">Case Study 03</div><h4>Brand Repositioning</h4><p>Franchisor type: Food and beverage brand, established system</p><p><b>Outcome:</b> Rebuilt pipeline and re-energized franchisee recruitment</p></div>
  <div class="foot">OUTPOST LATTICE ADVISORS</div><div class="pg">12</div>
</section>

<!-- 13 Enterprise value -->
<section class="slide" style="left:46px;top:797px">
  <div class="eyebrow">Enterprise Value</div>
  <h2 class="title">Building Enterprise Value Through Franchise Growth</h2>
  <p class="lede" style="top:37px">Franchise growth creates recurring royalty revenue and increases enterprise value.</p>
  <div class="tlabel" style="left:13.9px">EXAMPLE GROWTH SCENARIO</div>
  <table class="vtable" style="left:13.9px;width:125.4px">
    <tr><th style="width:45px">Stage</th><th style="width:29px">Units</th><th>Annual Royalty Revenue</th></tr>
    <tr><td>Early Growth</td><td>20</td><td>$165,000</td></tr>
    <tr><td>Growth Stage</td><td>63</td><td>$1,470,000</td></tr>
  </table>
  <div class="tlabel" style="left:148.1px">ILLUSTRATIVE VALUATION RANGE</div>
  <table class="vtable" style="left:148.1px;width:111.5px">
    <tr><th style="width:42px">Royalty Revenue</th><th>10x EBITDA</th><th>15x EBITDA</th></tr>
    <tr><td>$165,000</td><td>$1.65M</td><td>$2.48M</td></tr>
    <tr><td>$1,470,000</td><td>$14.7M</td><td>$22.05M</td></tr>
  </table>
  <div class="takeaway"><h5>Key Takeaway</h5><p>Franchise growth is not just about selling franchises. It is about creating recurring royalty revenue that can significantly increase the value of the franchise system.</p></div>
  <div class="foot">OUTPOST LATTICE ADVISORS</div><div class="pg">13</div>
</section>

<!-- 14 Exit -->
<section class="slide dark" style="left:359px;top:797px">
  <div class="eyebrow">Exit Strategy</div>
  <h2 class="title">Creating Future Exit Opportunities</h2>
  <div class="xcard" style="left:14.4px"><div class="ico or"><svg><use href="#bank"/></svg></div><p>Private Equity Acquisition</p></div>
  <div class="xcard" style="left:69.3px"><div class="ico or"><svg><use href="#hand"/></svg></div><p>Strategic Buyer Acquisition</p></div>
  <div class="xcard" style="left:124.2px"><div class="ico or"><svg><use href="#refresh"/></svg></div><p style="margin-top:16px">Recapitalization</p></div>
  <div class="xcard" style="left:179px"><div class="ico or"><svg><use href="#users"/></svg></div><p>Family Succession</p></div>
  <div class="xcard" style="left:234px"><div class="ico or"><svg><use href="#chart"/></svg></div><p style="margin-top:16px">Long-Term Cash Flow Ownership</p></div>
  <div class="goldbar">Every franchise sold today may contribute to enterprise value tomorrow.</div>
  <div class="foot">OUTPOST LATTICE ADVISORS</div><div class="pg">14</div>
</section>

<!-- 15 Different -->
<section class="slide" style="left:672px;top:797px">
  <div class="eyebrow">What Sets Us Apart</div>
  <h2 class="title">Why Outpost Lattice Advisors Is Different</h2>
  <div class="dcard" style="left:13.9px;top:42.7px"><div class="ico"><svg><use href="#db"/></svg></div><p>Fractional Cost Model</p></div>
  <div class="dcard" style="left:82.6px;top:42.7px"><div class="ico"><svg><use href="#rocket"/></svg></div><p>Immediate Execution</p></div>
  <div class="dcard" style="left:150.8px;top:42.7px"><div class="ico"><svg><use href="#chart"/></svg></div><p>500+ Franchise Sales</p></div>
  <div class="dcard" style="left:219.5px;top:42.7px"><div class="ico"><svg><use href="#award"/></svg></div><p>30+ Years' Experience</p></div>
  <div class="dcard" style="left:13.9px;top:92.4px"><div class="ico"><svg><use href="#network"/></svg></div><p style="margin-top:6px">Established Broker Network</p></div>
  <div class="dcard" style="left:82.6px;top:92.4px"><div class="ico"><svg><use href="#gear"/></svg></div><p>Proven Growth Systems</p></div>
  <div class="dcard hi" style="left:150.8px;top:92.4px"><div class="ico"><svg style="color:var(--orange)"><use href="#hand"/></svg></div><p>Strategic Growth Partner</p></div>
  <div class="foot">OUTPOST LATTICE ADVISORS</div><div class="pg">15</div>
</section>

<!-- 16 Engagement -->
<section class="slide" style="left:46px;top:985px">
  <div class="eyebrow">Engagement Options</div>
  <h2 class="title">Engagement Options</h2>
  <p class="lede" style="top:37.5px">Flexible ways to work together, based on where your brand is today.</p>
  <div class="ecard" style="left:13.9px"><div class="ico"><svg><use href="#hand"/></svg></div><h4>Franchise Sales Outsourcing</h4><p>A fully managed, fractional sales team driving candidate flow.</p></div>
  <div class="ecard" style="left:69.9px"><div class="ico"><svg><use href="#network"/></svg></div><h4>Broker Network Development</h4><p>Building and managing your referral relationships.</p></div>
  <div class="ecard hi" style="left:126px"><div class="ico"><svg style="color:var(--orange)"><use href="#chart"/></svg></div><h4>Franchise Growth Consulting</h4><p>Strategic guidance on scaling your development function.</p></div>
  <div class="ecard" style="left:182px"><div class="ico"><svg><use href="#globe"/></svg></div><h4>Franchise Expansion Strategy</h4><p>Territory planning and multi-market growth roadmaps.</p></div>
  <div class="ecard" style="left:238.8px"><div class="ico"><svg><use href="#doc"/></svg></div><h4>Franchise Development Advisory</h4><p>Ongoing counsel for founders and leadership teams.</p></div>
  <div class="foot">OUTPOST LATTICE ADVISORS</div><div class="pg">16</div>
</section>

<!-- 17 Summary -->
<section class="slide" style="left:359px;top:985px">
  <div class="eyebrow">Summary</div>
  <h2 class="title">Bringing It All Together</h2>
  <p class="lede" style="top:37.5px">A fast-deployed development partner, built to turn franchise growth into lasting enterprise value.</p>
  <div class="sumbox" style="left:13.9px">
    <div class="sumitem"><span class="tag yes"><svg><use href="#check"/></svg></span>A fractional team that replaces the cost and risk of an internal hire</div>
    <div class="sumitem"><span class="tag yes"><svg><use href="#check"/></svg></span>A proven process that moves leads from first contact to franchise award</div>
    <div class="sumitem"><span class="tag yes"><svg><use href="#check"/></svg></span>Multiple paths to a future exit, kept open by disciplined growth</div>
  </div>
  <div class="sumbox" style="left:150.2px">
    <div class="sumitem"><span class="tag yes"><svg><use href="#check"/></svg></span>Immediate access to 30+ years of broker network relationships</div>
    <div class="sumitem"><span class="tag yes"><svg><use href="#check"/></svg></span>Recurring royalty revenue that compounds enterprise value over time</div>
    <div class="sumitem"><span class="tag yes"><svg><use href="#check"/></svg></span>Flexible engagement options tailored to where your brand is today</div>
  </div>
  <div class="quote">Outpost Lattice Advisors gives your brand a complete development capability without the time, cost, or risk of building one internally.</div>
  <div class="foot">OUTPOST LATTICE ADVISORS</div><div class="pg">17</div>
</section>

<!-- 18 Call to action -->
<section class="slide dark" style="left:672px;top:985px">
  <div class="brand" style="left:18.5px;top:27px">OUTPOST LATTICE ADVISORS</div>
  <h2 class="cta-title">Let's Build Your Growth Plan</h2>
  <p class="cta-sub">Schedule a Franchise Growth Strategy Consultation</p>
  <div class="cta-btn">Book a Strategy Call</div>
  <div class="contact" style="top:126.5px"><div class="ico or"><svg><use href="#mail"/></svg></div>info@outpostlatticeadvisors.example</div>
  <div class="contact" style="top:139px"><div class="ico or"><svg><use href="#pin"/></svg></div>418 Meridian Way, Ste 2, Harbor City, FL 30001</div>
  <div class="pg">18</div>
</section>

</main>
</body>
</html>
```